どの案も素敵でしたが、こちらの作品が最もイメージにあっていました。
皆様ご提案ありがとうございました。どれも個性的で良い提案ばかりでした。また機会があれば依頼させていただきますのでよろしくお願いいたします。
書籍の表紙デザイン案のお願い のびのび気分整理術 バナー作成・バナーデザインの仕事の依頼

```html
<!DOCTYPE html>
<html lang="ja">
<head>
<meta charset="UTF-8">
<title>のびのび気分整理術</title>
<link rel="stylesheet" href="https://fonts.googleapis.com/css2?family=M+PLUS+Rounded+1c:wght@500;700;800;900&display=swap">
<style>
  :root {
    --paper: #ffffff;
    --ink: #3a3a3a;
    --title-gray: #595959;
    --pink: #ee6f9c;
    --band: #f3d3da;
    --accent-wave: #4a7fd6;
    --sparkle: #f7ea5c;
    --art-hair: #f4b3c6;
    --art-skirt: #f8d9e2;
    --art-soft: #fcefF3;
  }
  * { margin: 0; padding: 0; box-sizing: border-box; }
  html, body { width: 752px; height: 1200px; overflow: hidden; background: var(--paper); }
  .cover {
    position: relative;
    width: 752px;
    height: 1200px;
    background: var(--paper);
    font-family: "M PLUS Rounded 1c", sans-serif;
    color: var(--ink);
    overflow: hidden;
  }
  .tagline {
    position: absolute;
    top: 64px; left: 0; width: 100%;
    text-align: center;
    font-size: 33px;
    font-weight: 800;
    letter-spacing: 1px;
    line-height: 1;
  }
  .title { font-weight: 900; }
  .title span {
    position: absolute;
    left: 0; width: 100%;
    text-align: center;
    line-height: 1;
    paint-order: stroke fill;
    -webkit-text-stroke: 12px #fff;
  }
  .title-top {
    top: 136px;
    font-size: 98px;
    color: var(--pink);
    letter-spacing: 2px;
    text-shadow: 5px 6px 0 rgba(0,0,0,0.14);
  }
  .title-main {
    top: 246px;
    font-size: 82px;
    color: var(--title-gray);
    letter-spacing: 4px;
    text-shadow: 5px 6px 0 rgba(0,0,0,0.2);
  }
  .illustration {
    position: absolute;
    top: 350px; left: 176px;
    width: 400px; height: 615px;
    border-radius: 180px 180px 40px 40px;
    background:
      radial-gradient(ellipse 32% 16% at 50% 18%, var(--art-hair) 0%, rgba(244,179,198,0) 100%),
      radial-gradient(ellipse 52% 20% at 50% 60%, var(--art-skirt) 0%, rgba(248,217,226,0) 100%),
      linear-gradient(180deg, var(--art-soft) 0%, #fdf6f8 100%);
  }
  .sparkles { position: absolute; inset: 0; pointer-events: none; }
  .sparkle { fill: var(--sparkle); }
  .band {
    position: absolute;
    left: 0; bottom: 0;
    width: 752px; height: 235px;
    background: var(--band);
  }
  .subtitle {
    position: absolute;
    top: 34px; left: 40px;
    font-size: 50px;
    font-weight: 900;
    line-height: 1;
    display: flex;
    align-items: center;
  }
  .subtitle .circle {
    display: inline-flex;
    align-items: center; justify-content: center;
    width: 62px; height: 62px;
    border-radius: 50%;
    background: var(--pink);
    color: #fff;
    font-size: 44px;
    margin-right: 4px;
  }
  .subtitle .light { position: relative; color: var(--pink); }
  .subtitle .light svg {
    position: absolute;
    left: 2px; bottom: -14px;
    width: 46px; height: 12px;
  }
  .headline {
    position: absolute;
    top: 120px; left: 40px;
    font-size: 57px;
    font-weight: 900;
    line-height: 1;
    letter-spacing: 0;
  }
</style>
</head>
<body>
<main class="cover">
  <p class="tagline">＼ストレスを受け流すマインド方法／</p>
  <h1 class="title">
    <span class="title-top">のびのび</span>
    <span class="title-main">気分整理術</span>
  </h1>
  <div class="illustration" role="img" aria-label="両手を広げて笑顔で立つピンクの髪とピンクのスカートの女性のイラスト"></div>
  <svg class="sparkles" viewBox="0 0 752 1200" aria-hidden="true">
    <defs>
      <path id="star" d="M0 -1 Q0.12 -0.12 1 0 Q0.12 0.12 0 1 Q-0.12 0.12 -1 0 Q-0.12 -0.12 0 -1Z"/>
    </defs>
    <use href="#star" class="sparkle" transform="translate(108 165) scale(44)"/>
    <use href="#star" class="sparkle" transform="translate(640 268) scale(44)"/>
    <use href="#star" class="sparkle" transform="translate(566 460) scale(32)"/>
    <use href="#star" class="sparkle" transform="translate(628 528) scale(20)"/>
    <use href="#star" class="sparkle" transform="translate(150 646) scale(34)"/>
    <use href="#star" class="sparkle" transform="translate(66 720) scale(24)"/>
  </svg>
  <section class="band">
    <p class="subtitle">
      <span class="circle">心</span>を<span class="light">軽<svg viewBox="0 0 46 12" preserveAspectRatio="none"><path d="M2 6 Q7 1 12 6 T23 6 T34 6 T44 6" fill="none" stroke="var(--accent-wave)" stroke-width="3" stroke-linecap="round"/></svg></span>くする
    </p>
    <p class="headline">メンタルコントロール術</p>
  </section>
</main>
</body>
</html>
```